Multifamily Property Needs a Flyer Design

I need a flyer that announces and highlights the renovations we are doing at an apartment community. The flyer needs to not only list the upgrades, but also communicate the renovation is an express upgrade. I've attached the color scheme we would like to use on the flyer (mustard and gray) and I've attached the property logo, Birch Hollowmere Apartments. Here are the renovations that are going to be done and more information that needs to be included on the flyer:Tagline: Now You See It, Now You Don’tLake Castleton renovation will soon be underway and ready for move-in by early November. We will be launching an Express Upgrade Service so that renovations will be completed in a blink of an eye. Contact the Leasing Office for more details, 555-302-7746. * All New Flooring* All New Kitchen, including New Countertops New Cabinets New Hardware New Appliances* New Designer Lighting and Plumbing Fixtures* New Bathroom Upgrades, including New Countertops New Cabinets New HardwareComing 2018:*New Dog Park*New Clubhouse*All New Pool Furniture and Accessories

```html
<!DOCTYPE html>
<html lang="en">
<head>
<meta charset="utf-8">
<title>Birch Hollowmere Renovation Flyer</title>
<link href="https://fonts.googleapis.com/css2?family=Questrial&display=swap" rel="stylesheet">
<style>
  :root {
    --mustard: #e6bd37;
    --mustard-text: #f0c53c;
    --charcoal: #1e1615;
    --ink: #2b2118;
    --white: #ffffff;
    --paper: #ffffff;
    --wall: #e8d9bd;
    --wood-dark: #4a2814;
    --wood: #7a4420;
    --counter: #cf9440;
    --floor: #dccbaa;
  }
  * { margin: 0; padding: 0; box-sizing: border-box; }
  html, body { width: 853px; height: 1200px; overflow: hidden; background: var(--paper); }
  body { font-family: "Questrial", sans-serif; position: relative; }

  .flyer { position: absolute; left: 35px; top: 35px; width: 783px; height: 1130px; overflow: hidden; background: var(--charcoal); }

  .hero-photo {
    position: absolute; left: 0; top: 0; width: 783px; height: 640px;
    background:
      linear-gradient(90deg, rgba(74,40,20,0.85) 0%, rgba(74,40,20,0.35) 16%, rgba(74,40,20,0) 32%, rgba(74,40,20,0) 70%, rgba(74,40,20,0.4) 84%, rgba(74,40,20,0.85) 100%),
      linear-gradient(180deg, var(--wall) 0%, #efe3c8 35%, var(--counter) 48%, var(--wood) 56%, var(--wood-dark) 70%, #b59b74 80%, var(--floor) 100%);
  }

  .diagonal { position: absolute; left: 0; top: 0; width: 783px; height: 1130px; }

  .intro { position: absolute; left: 48px; top: 640px; width: 340px; text-align: center; color: var(--white); }
  .tagline { font-size: 34px; line-height: 47px; color: var(--mustard-text); font-weight: 400; }
  .intro-copy { margin-top: 12px; font-size: 15px; line-height: 22.4px; }

  .coming-soon {
    position: absolute; left: 62px; top: 901px; width: 299px; height: 130px;
    border: 1px solid var(--mustard); text-align: center; color: var(--white);
    font-size: 18px; line-height: 26px; padding-top: 16px;
  }
  .coming-title {
    position: absolute; top: -14px; left: 50%; transform: translateX(-50%);
    background: var(--charcoal); padding: 0 12px; color: var(--mustard-text);
    font-size: 18px; font-weight: 400; white-space: nowrap;
  }
  .coming-list { list-style: none; }

  .contact { position: absolute; left: 30px; top: 1050px; width: 376px; text-align: center; color: var(--white); font-size: 18.5px; line-height: 26px; }
  .contact-phone { color: var(--mustard-text); font-weight: 700; }

  .upgrades {
    position: absolute; left: 449px; top: 547px; width: 293px; height: 401px;
    background: var(--mustard); color: var(--ink); font-size: 17.5px; line-height: 24.4px;
    padding: 48px 8px 0 26px;
  }
  .upgrade-list { list-style: none; }
  .upgrade-item { position: relative; padding-left: 23px; margin-bottom: 6px; }
  .upgrade-item::before { content: ""; position: absolute; left: 0; top: 10px; width: 5px; height: 5px; border-radius: 50%; background: var(--ink); }
  .sub-list { list-style: none; padding-left: 13px; }

  .brand { position: absolute; left: 449px; top: 975px; width: 293px; text-align: center; color: var(--white); }
  .brand-mark { width: 50px; height: 50px; border-radius: 50%; background: var(--white); margin: 0 auto 24px; }
  .brand-name { font-size: 24px; letter-spacing: 1px; text-transform: uppercase; }
  .brand-sub { font-size: 12.5px; letter-spacing: 3px; text-transform: uppercase; margin-top: 6px; }

  .footer-bar { position: absolute; left: 449px; top: 1120px; width: 293px; height: 10px; background: var(--mustard); }
</style>
</head>
<body>
<main class="flyer">
  <div class="hero-photo" role="img" aria-label="Photo of an apartment kitchen with dark wood cabinets, warm countertops, a double sink under a window, a white stove and a tiled floor"></div>

  <svg class="diagonal" viewBox="0 0 783 1130" aria-hidden="true">
    <polygon points="0,617 783,520 783,1130 0,1130" fill="var(--charcoal)"/>
    <polygon points="150,598 783,522 783,542 0,617" fill="var(--mustard)"/>
  </svg>

  <section class="intro">
    <h1 class="tagline">Now You See It,<br>Now You Don’t</h1>
    <p class="intro-copy">Birch Hollowmere renovation will soon be underway and ready for move-in by early November. We will be launching an Express Upgrade Service so that renovations will be completed in a blink of an eye.</p>
  </section>

  <section class="coming-soon">
    <h2 class="coming-title">Coming 2018</h2>
    <ul class="coming-list">
      <li>New Dog Park</li>
      <li>New Clubhouse</li>
      <li>All New Pool Furniture<br>and Accessories</li>
    </ul>
  </section>

  <p class="contact">Contact the Leasing Office<br>for more details, <span class="contact-phone">555-302-7746</span></p>

  <section class="upgrades">
    <ul class="upgrade-list">
      <li class="upgrade-item">All New Flooring</li>
      <li class="upgrade-item">All New Kitchen, including
        <ul class="sub-list"><li>New Countertops</li><li>New Cabinets</li><li>New Hardware</li><li>New Appliances</li></ul>
      </li>
      <li class="upgrade-item">New Designer Lighting<br>and Plumbing Fixtures</li>
      <li class="upgrade-item">New Bathroom Upgrades,
        <ul class="sub-list"><li>including</li><li>New Countertops</li><li>New Cabinets</li><li>New Hardware</li></ul>
      </li>
    </ul>
  </section>

  <div class="brand">
    <div class="brand-mark"></div>
    <p class="brand-name">Birch Hollowmere</p>
    <p class="brand-sub">Apartment Homes</p>
  </div>

  <div class="footer-bar"></div>
</main>
</body>
</html>
```